Flyer in Creole

Instructions for Designer
Objective: Create two versions of the flyer for Bricamel dental services: one in French and one in Creole. Target audience is elders of the haitian community in Montreal so include picture of an older person with a darker skin complexion.

I have included our original flyer.

Bricamel - Sèvis Dantè pou Granmoun Aje
Nou ofri swen dantè san frè pou moun 65 an e plis!

La Clinique Dentaire Bricamel gen kè kontan patisipe nan Pwogram Dantè Solèvan (PDSV). Si w gen 65 an oubyen plis, ou ka resevwa swen dantè gratis, san frè siplemantè si w kalifye.

Kijan pou Kalifye?

Si w gen 65 an ou plis, ou ka jwenn tretman dantè san frè.
Vizite: https://www.swendanteprogram.example/aplike/dantè.html pou w aplike epi w konnen si w kalifye.
Sèvis Nou Ofri:

Netwayaj dantè: Sante bouch ou enpòtan, fè yon netwayaj pwofesyonèl pou prezève sante dantè w.
Egzamen ak radyografi: Pran yon randevou pou yon egzamen konplè ak radyografi.
Ekstraksyon dantè: Retire dan ki domaje oswa ki fè w mal.
Ijans dantè: Tretman rapid pou doulè, dan kase, oswa lòt ijans.
Pwotèz dantè konplè ak pasyèl: Nou ranplase dan ki manke yo pou yon bèl souri ak bon sante.
Rele Kounye a pou Fiks yon Randevou: 514-782-4695
Klinik Bricamel - 2863 Rue Marcoux-Belval E, 2yèm etaj, Montreal, QC H2K 3R8
Design Elements:
Use images that resonate with the Creole-speaking community.
Ensure the text is clear and accessible.

```html
<!DOCTYPE html>
<html lang="ht">
<head>
<meta charset="utf-8">
<title>Bricamel – Sèvis Dantè pou Granmoun Aje</title>
<link rel="stylesheet" href="https://fonts.googleapis.com/css2?family=Source+Serif+4:opsz,wght@8..60,400;8..60,600;8..60,700&family=Inter:wght@300;400&display=swap">
<style>
  :root {
    --navy: #263650;
    --navy-deep: #1f2d44;
    --sky: #a9c5f0;
    --sky-line: #9dbbe9;
    --white: #ffffff;
    --paper: #e4e4e4;
    --rule: #51627e;
    --photo-a: #8fa4bd;
    --photo-b: #c9d6e2;
    --photo-warm: #8a5a44;
    --serif: "Source Serif 4", Georgia, serif;
    --sans: "Inter", Arial, sans-serif;
  }
  * { margin: 0; padding: 0; box-sizing: border-box; }
  html, body { width: 1200px; height: 2173px; overflow: hidden; background: var(--paper); }
  .flyer {
    position: absolute; left: 50px; top: 374px;
    width: 932px; height: 1207px;
    transform: scale(1.1803); transform-origin: 0 0;
    background: var(--white); overflow: hidden;
    font-family: var(--sans); color: var(--navy);
  }
  .abs { position: absolute; }
  .hero-photo {
    left: 0; top: 22px; width: 932px; height: 445px;
    background: linear-gradient(120deg, var(--photo-warm) 0%, #b58e7a 22%, var(--photo-a) 45%, var(--photo-b) 70%, #aab9c9 100%);
  }
  .top-strip { left: 0; top: 0; width: 932px; height: 22px; background: var(--navy); }
  .logo-plate { left: 0; top: 0; }
  .brand {
    left: 55px; top: 18px;
    font-family: var(--serif); font-weight: 400; font-size: 84px; letter-spacing: -1px;
    color: var(--navy); line-height: 1;
  }
  .hero-panel { left: 0; top: 190px; }
  .hero-title {
    left: 57px; top: 212px;
    font-family: var(--serif); font-weight: 700; font-size: 47px; line-height: 46px;
    color: var(--sky);
  }
  .hero-sub {
    left: 57px; top: 310px;
    font-family: var(--serif); font-weight: 700; font-size: 28px; line-height: 30px;
    color: var(--white);
  }
  .hero-body {
    left: 57px; top: 378px; width: 470px;
    font-weight: 300; font-size: 16px; line-height: 21.5px; color: var(--white);
  }
  .services-panel {
    left: 560px; top: 517px; width: 372px; height: 690px;
    background: var(--navy); border-top-left-radius: 50px;
  }
  .bottom-band { left: 0; top: 1160px; width: 932px; height: 47px; background: var(--navy); }
  .left-sheet {
    left: 0; top: 492px; width: 556px; height: 688px;
    background: var(--white); border-bottom-right-radius: 30px;
  }
  .qualify-title {
    left: 57px; top: 522px;
    font-family: var(--serif); font-weight: 700; font-size: 32px; color: var(--navy);
  }
  .qualify-rule { left: 0; top: 572px; }
  .qualify-lead {
    left: 57px; top: 590px;
    font-family: var(--serif); font-weight: 700; font-size: 18px; line-height: 28px;
  }
  .qualify-link {
    left: 57px; top: 652px; width: 440px;
    font-size: 20px; line-height: 26px; font-weight: 400; word-break: break-all;
  }
  .qualify-tail {
    left: 57px; top: 708px;
    font-family: var(--serif); font-weight: 700; font-size: 18px;
  }
  .gallery {
    left: 55px; top: 752px; width: 462px;
    display: grid; grid-template-columns: 1fr 1fr; gap: 10px;
  }
  .gallery-tile {
    height: 119px; border: 3px solid var(--navy); border-radius: 9px;
  }
  .tile-1 { background: linear-gradient(135deg, #c7a58f, #e6ecf2 60%, #cfd8e2); }
  .tile-2 { background: linear-gradient(135deg, #8fb3c8, #c9d3dd 55%, #7d93b0); }
  .tile-3 { background: linear-gradient(135deg, #b86a45, #d9a27f 50%, #c7d2de); }
  .tile-4 { background: linear-gradient(135deg, #c07c55, #e2c2a8 45%, #7f9ab7); }
  .call-label {
    left: 76px; top: 1018px;
    font-family: var(--serif); font-weight: 700; font-size: 19px;
  }
  .call-number {
    left: 76px; top: 1046px; display: flex; align-items: center; gap: 8px;
    font-family: var(--serif); font-weight: 700; font-size: 50px; line-height: 1;
  }
  .address {
    left: 60px; top: 1115px; width: 812px; height: 46px;
    border: 3px solid var(--sky-line); border-radius: 23px; background: var(--white);
    display: flex; align-items: center; gap: 12px; padding-left: 26px;
    font-size: 20px; color: var(--navy);
  }
  .services-tab { left: 548px; top: 548px; }
  .services-tab-label {
    left: 548px; top: 548px; width: 338px; height: 58px;
    background: var(--sky); border-radius: 10px;
    display: flex; align-items: center; justify-content: center;
    font-family: var(--serif); font-weight: 700; font-size: 35px; color: var(--navy);
    box-shadow: 0 3px 6px rgba(0,0,0,.25);
  }
  .service-list { left: 600px; top: 628px; width: 282px; list-style: none; }
  .service {
    position: relative; padding-left: 43px;
    padding-bottom: 12px; margin-bottom: 12px;
    border-bottom: 1px solid var(--rule);
  }
  .service:last-child { border-bottom: none; }
  .service-tick { position: absolute; left: 2px; top: 2px; }
  .service-name {
    font-family: var(--serif); font-weight: 700; font-size: 21px; line-height: 22px; color: var(--white);
    margin-bottom: 6px;
  }
  .service-desc {
    font-weight: 300; font-size: 15.5px; line-height: 18px; color: #e8edf5;
  }
</style>
</head>
<body>
<div class="flyer">
  <div class="abs hero-photo" role="img" aria-label="Photo: smiling older man with a darker skin complexion in a dental chair, dentist in the background"></div>
  <div class="abs top-strip"></div>

  <svg class="abs logo-plate" width="480" height="135" viewBox="0 0 480 135">
    <polygon points="0,0 475,0 436,133 0,133" fill="#ffffff"/>
  </svg>
  <div class="abs brand">Bricamel</div>

  <svg class="abs hero-panel" width="610" height="302" viewBox="0 0 610 302">
    <polygon points="0,0 440,0 585,277 0,277" fill="#263650"/>
    <polygon points="585,277 610,277 585,302 0,302 0,277" fill="#ffffff"/>
    <polygon points="585,277 608,277 590,300" fill="#a9c5f0"/>
  </svg>
  <h1 class="abs hero-title">Sèvis Dantè pou<br>Granmoun Aje</h1>
  <p class="abs hero-sub">Nou ofri swen dantè san frè<br>pou moun 65 an e plis!</p>
  <p class="abs hero-body">La Clinique Dentaire Bricamel gen kè kontan patisipe nan Pwogram Dantè Solèvan (PDSV). Si w gen 65 an oubyen plis, ou ka resevwa swen dantè gratis, san frè siplemantè si w kalifye.</p>

  <div class="abs services-panel"></div>
  <div class="abs bottom-band"></div>
  <div class="abs left-sheet"></div>

  <h2 class="abs qualify-title">Kijan pou Kalifye?</h2>
  <svg class="abs qualify-rule" width="455" height="10" viewBox="0 0 455 10">
    <line x1="0" y1="5" x2="448" y2="5" stroke="#263650" stroke-width="1.5"/>
    <circle cx="449" cy="5" r="3" fill="#263650"/>
  </svg>
  <p class="abs qualify-lead">Si w gen 65 an ou plis, ou ka jwenn<br>tretman dantè san frè. Vizite:</p>
  <p class="abs qualify-link">https://www.swendanteprogram.example/<br>aplike/dantè.html</p>
  <p class="abs qualify-tail">pou w aplike epi w konnen si w kalifye.</p>

  <div class="abs gallery">
    <div class="gallery-tile tile-1" role="img" aria-label="Photo: older woman smiling with her dentist"></div>
    <div class="gallery-tile tile-2" role="img" aria-label="Photo: older man during a dental exam"></div>
    <div class="gallery-tile tile-3" role="img" aria-label="Photo: dentist showing a denture to a patient"></div>
    <div class="gallery-tile tile-4" role="img" aria-label="Photo: smiling older woman in a dental chair"></div>
  </div>

  <p class="abs call-label">Rele Kounye a pou Fiks yon Randevou:</p>
  <div class="abs call-number">
    <svg width="40" height="40" viewBox="0 0 40 40">
      <circle cx="20" cy="20" r="17.5" fill="none" stroke="#263650" stroke-width="3"/>
      <path d="M14 11c1-1 2.5-1 3.2.2l1.6 2.8c.5.9.2 1.9-.6 2.5l-1.1.8c.9 2.3 2.6 4 4.9 4.9l.8-1.1c.6-.8 1.6-1.1 2.5-.6l2.8 1.6c1.2.7 1.2 2.2.2 3.2l-1.2 1.2c-1.2 1.2-3 1.5-4.5.8-4.6-2.1-8.3-5.8-10.4-10.4-.7-1.5-.4-3.3.8-4.5z" fill="#263650"/>
    </svg>
    <span>514-782-4695</span>
  </div>

  <div class="abs address">
    <svg width="16" height="21" viewBox="0 0 16 21">
      <path d="M8 0C3.6 0 0 3.5 0 7.9 0 13.5 8 21 8 21s8-7.5 8-13.1C16 3.5 12.4 0 8 0zm0 11a3 3 0 1 1 0-6 3 3 0 0 1 0 6z" fill="#263650"/>
    </svg>
    <span>Klinik Bricamel - 2863 Rue Marcoux-Belval E, 2yèm etaj, Montreal, QC H2K 3R8</span>
  </div>

  <svg class="abs services-tab" width="20" height="80" viewBox="0 0 20 80">
    <polygon points="0,50 12,58 12,72 0,66" fill="#7f9fcf"/>
  </svg>
  <div class="abs services-tab-label">Sèvis Nou Ofri:</div>

  <ul class="abs service-list">
    <li class="service">
      <svg class="service-tick" width="24" height="24" viewBox="0 0 24 24"><circle cx="12" cy="12" r="12" fill="#a9c5f0"/><path d="M6.5 12.5l3.6 3.5 7.4-7.6" fill="none" stroke="#263650" stroke-width="2.6" stroke-linecap="round" stroke-linejoin="round"/></svg>
      <h3 class="service-name">Netwayaj dantè:</h3>
      <p class="service-desc">Sante bouch ou enpòtan,<br>fè yon netwayaj pwofesyonèl<br>pou prezève sante dantè w.</p>
    </li>
    <li class="service">
      <svg class="service-tick" width="24" height="24" viewBox="0 0 24 24"><circle cx="12" cy="12" r="12" fill="#a9c5f0"/><path d="M6.5 12.5l3.6 3.5 7.4-7.6" fill="none" stroke="#263650" stroke-width="2.6" stroke-linecap="round" stroke-linejoin="round"/></svg>
      <h3 class="service-name">Egzamen ak radyografi:</h3>
      <p class="service-desc">Pran yon randevou pou yon<br>egzamen konplè ak radyografi.</p>
    </li>
    <li class="service">
      <svg class="service-tick" width="24" height="24" viewBox="0 0 24 24"><circle cx="12" cy="12" r="12" fill="#a9c5f0"/><path d="M6.5 12.5l3.6 3.5 7.4-7.6" fill="none" stroke="#263650" stroke-width="2.6" stroke-linecap="round" stroke-linejoin="round"/></svg>
      <h3 class="service-name">Ekstraksyon dantè:</h3>
      <p class="service-desc">Retire dan ki domaje oswa<br>ki fè w mal.</p>
    </li>
    <li class="service">
      <svg class="service-tick" width="24" height="24" viewBox="0 0 24 24"><circle cx="12" cy="12" r="12" fill="#a9c5f0"/><path d="M6.5 12.5l3.6 3.5 7.4-7.6" fill="none" stroke="#263650" stroke-width="2.6" stroke-linecap="round" stroke-linejoin="round"/></svg>
      <h3 class="service-name">Ijans dantè:</h3>
      <p class="service-desc">Tretman rapid pou doulè, dan<br>kase, oswa lòt ijans.</p>
    </li>
    <li class="service">
      <svg class="service-tick" width="24" height="24" viewBox="0 0 24 24"><circle cx="12" cy="12" r="12" fill="#a9c5f0"/><path d="M6.5 12.5l3.6 3.5 7.4-7.6" fill="none" stroke="#263650" stroke-width="2.6" stroke-linecap="round" stroke-linejoin="round"/></svg>
      <h3 class="service-name">Pwotèz dantè konplè<br>ak pasyèl:</h3>
      <p class="service-desc">Nou ranplase dan ki manke yo<br>pou yon bèl souri ak bon sante.</p>
    </li>
  </ul>
</div>
</body>
</html>
```